Business Card Design

We need a business card design for a new company based in Melbourne Australia. We are financial broker in finance industry. We provide a wide range of finance solutions to our clients including home loans, commercial loans, business facilities, car loans, equipment loans, invoice finance, etc. The company name is from director's personal name. We would like to have a new company logo that includes TK.

Industry/Entity Type

Business

Contact Information for Business Card

company name: TK & Co Finance Pty Ltd
person's name: Desmond Okafor
role: Managing Director
Mobile: 0417 638 294
fax: 03 9561 4472
Email: desmond.okafor@tkcolending.example
Address: Suite 5/418 Marlow Avenue Elmvale Vic 3174
Credit Licence No.: 718249

```html
<!DOCTYPE html>
<html lang="en">
<head>
<meta charset="utf-8">
<title>TK &amp; Co Finance – Business Card</title>
<link rel="stylesheet" href="https://fonts.googleapis.com/css2?family=Lato:wght@400;700&family=Source+Sans+3:wght@400;600&display=swap">
<style>
  :root {
    --stage: #424242;
    --card-front: #000000;
    --card-back: #070707;
    --brand-red: #e8141b;
    --mark-grey: #4a4a4a;
    --mark-light: #cfcfcf;
    --text-white: #ffffff;
    --text-muted: #bdbdbd;
    --divider: #262626;
  }
  * { margin: 0; padding: 0; box-sizing: border-box; }
  html, body { width: 1200px; height: 900px; overflow: hidden; }
  body {
    position: relative;
    background: var(--stage);
    font-family: "Source Sans 3", "Myriad Pro", sans-serif;
    color: var(--text-white);
  }
  .card {
    position: absolute;
    top: 271px;
    width: 457px;
    height: 281px;
    border-radius: 14px;
    overflow: hidden;
  }
  .card--front { left: 137px; background: var(--card-front); }
  .card--back { left: 626px; background: var(--card-back); }

  /* front */
  .front-wordmark {
    position: absolute;
    left: 40px;
    top: 82px;
    font-family: "Lato", sans-serif;
    font-weight: 400;
    font-size: 104px;
    line-height: 1;
    letter-spacing: -2px;
    color: var(--mark-grey);
  }
  .front-divider {
    position: absolute;
    left: 225px;
    top: 50px;
    width: 1px;
    height: 170px;
    background: var(--divider);
  }
  .details {
    position: absolute;
    left: 241px;
    top: 47px;
    width: 210px;
  }
  .person-name {
    font-weight: 600;
    font-size: 16.5px;
    line-height: 20px;
    color: var(--brand-red);
  }
  .person-role {
    font-size: 13px;
    line-height: 16px;
  }
  .contact-list {
    list-style: none;
    margin-top: 22px;
  }
  .contact-item {
    position: relative;
    padding-left: 17px;
    font-size: 12.5px;
    line-height: 17px;
    margin-bottom: 2px;
  }
  .contact-item--email { font-size: 11px; letter-spacing: -0.1px; }
  .contact-icon {
    position: absolute;
    left: 2px;
    top: 4px;
    width: 9px;
    height: 9px;
    fill: var(--brand-red);
  }
  .licence {
    margin-top: 16px;
    font-size: 12.5px;
    line-height: 16px;
  }

  /* back */
  .back-wordmark {
    position: absolute;
    left: 0;
    right: 0;
    top: 72px;
    text-align: center;
    font-family: "Lato", sans-serif;
    font-weight: 400;
    font-size: 74px;
    line-height: 1;
    letter-spacing: -1px;
    color: var(--mark-light);
  }
  .company-name {
    position: absolute;
    left: 0;
    right: 0;
    top: 157px;
    text-align: center;
    font-family: "Lato", sans-serif;
    font-size: 24px;
    line-height: 30px;
    letter-spacing: 0.3px;
  }
  .company-suffix {
    position: absolute;
    right: 118px;
    top: 187px;
    font-family: "Lato", sans-serif;
    font-size: 13px;
    color: var(--text-muted);
  }
</style>
</head>
<body>

<section class="card card--front" aria-label="Card front">
  <div class="front-wordmark">TK</div>
  <div class="front-divider"></div>
  <div class="details">
    <p class="person-name">Desmond Okafor</p>
    <p class="person-role">Managing Director</p>
    <ul class="contact-list">
      <li class="contact-item">
        <svg class="contact-icon" viewBox="0 0 10 10" aria-hidden="true"><path d="M2 0.5 L3.6 2.6 L2.8 3.6 Q4 6 6.4 7.2 L7.4 6.4 L9.5 8 L8.3 9.5 Q1 7.5 0.5 1.7 Z"/></svg>
        0417 638 294
      </li>
      <li class="contact-item">
        <svg class="contact-icon" viewBox="0 0 10 10" aria-hidden="true"><path d="M2.5 0.5 H7.5 V3 H9.5 V8 H0.5 V3 H2.5 Z M3.5 1.5 V3 H6.5 V1.5 Z M2.5 5 V9.5 H7.5 V5 Z" fill-rule="evenodd"/></svg>
        03 9561 4472
      </li>
      <li class="contact-item contact-item--email">
        <svg class="contact-icon" viewBox="0 0 10 10" aria-hidden="true"><path d="M0.5 2 H9.5 V8.5 H0.5 Z M1.2 2.6 L5 5.6 L8.8 2.6" fill-rule="evenodd"/></svg>
        desmond.okafor@tkcolending.example
      </li>
      <li class="contact-item">
        <svg class="contact-icon" viewBox="0 0 10 10" aria-hidden="true"><path d="M5 0.2 A3.6 3.6 0 0 1 8.6 3.8 Q8.6 6 5 9.8 Q1.4 6 1.4 3.8 A3.6 3.6 0 0 1 5 0.2 Z M5 2.5 A1.3 1.3 0 1 0 5 5.1 A1.3 1.3 0 1 0 5 2.5 Z" fill-rule="evenodd"/></svg>
        Suite 5/418 Marlow Avenue<br>Elmvale Vic 3174
      </li>
    </ul>
    <p class="licence">Credit Licence No.: 718249</p>
  </div>
</section>

<section class="card card--back" aria-label="Card back">
  <div class="back-wordmark">TK</div>
  <p class="company-name">TK &amp; CO FINANCE</p>
  <p class="company-suffix">Pty Ltd</p>
</section>

</body>
</html>
```